Marlowe Holdings LLC - Business Cards

Need the following information on the cards:

Name: Dean R Vossler
Title: Chief Executive Manager

Business address:
412 N Ridgeview Lane #118
Elm Harbor, Il 60412

Phone: (555) 555-0148 - Business
KPV FFL license number: 5-21-xxx-xx-xx-04519
Email: dean.vossler@marloweholdingsffl.com

Target Market(s)

Firearm owners

Industry/Entity Type

Firearms industry,

Contact Information for Business Card

Contact number, name and title, web page address, email, business address and kpv license number,

Requirements
Must have
• Name, title, business address, phone numbers, KPV license numbers, web page address and email address.
Nice to have
• Cellphone number,

```html
<!DOCTYPE html>
<html lang="en">
<head>
<meta charset="utf-8">
<title>Marlowe Holdings LLC – Business Cards</title>
<link rel="stylesheet" href="https://fonts.googleapis.com/css2?family=Lexend:wght@500;600&family=Open+Sans:wght@300;400;600&display=swap">
<style>
  :root {
    --blue: #3a87c7;
    --blue-2: #6a9bd2;
    --blue-3: #86acdc;
    --blue-4: #a9c2e6;
    --ink: #151515;
    --text: #3a3a3a;
    --paper: #ffffff;
    --backdrop: #e8e9eb;
  }
  * { box-sizing: border-box; margin: 0; padding: 0; }
  html, body { width: 1200px; height: 1000px; overflow: hidden; }
  body {
    background: var(--backdrop);
    font-family: "Open Sans", Arial, sans-serif;
    color: var(--text);
    position: relative;
  }
  .card {
    position: absolute;
    left: 290px;
    width: 620px;
    height: 354px;
    background: var(--paper);
    box-shadow: 0 6px 18px rgba(0,0,0,0.18);
    overflow: hidden;
  }
  .card--front { top: 116px; }
  .card--back { top: 530px; }
  .card__stripes {
    position: absolute;
    left: 0; top: 0;
    width: 100%; height: 100%;
  }
  .brand-mark {
    position: absolute;
    display: flex;
    flex-direction: column;
    align-items: center;
    gap: 10px;
    font-family: "Lexend", Arial, sans-serif;
    font-weight: 600;
    color: var(--blue);
    text-align: center;
    line-height: 1.1;
    white-space: nowrap;
  }
  .brand-mark__dot {
    border-radius: 50%;
    border: 3px solid var(--ink);
  }
  .card--front .brand-mark {
    left: 180px; top: 98px; width: 260px;
    font-size: 17px;
  }
  .card--front .brand-mark__dot { width: 76px; height: 76px; }
  .company-name {
    position: absolute;
    left: 0; right: 0; top: 230px;
    text-align: center;
    font-family: "Lexend", Arial, sans-serif;
    font-weight: 600;
    font-size: 37px;
    color: var(--ink);
    letter-spacing: -0.3px;
    white-space: nowrap;
  }
  .card--back .brand-mark {
    left: 30px; top: 62px; width: 200px;
    font-size: 16px;
  }
  .card--back .brand-mark__dot { width: 110px; height: 110px; }
  .contact-name {
    position: absolute;
    right: 38px; top: 40px;
    font-family: "Lexend", Arial, sans-serif;
    font-weight: 600;
    font-size: 30px;
    color: var(--ink);
    letter-spacing: -0.2px;
    white-space: nowrap;
  }
  .contact-title {
    position: absolute;
    right: 38px; top: 76px;
    font-size: 12px;
    color: var(--blue);
    letter-spacing: 0.2px;
    white-space: nowrap;
  }
  .side-tab {
    position: absolute;
    right: 0; top: 33px;
    width: 16px; height: 66px;
    background: var(--blue);
    border-radius: 6px 0 0 6px;
  }
  .contact-list {
    position: absolute;
    right: 36px; top: 130px;
    list-style: none;
    font-weight: 300;
    font-size: 15px;
    color: var(--text);
  }
  .contact-list li {
    display: flex;
    justify-content: flex-end;
    align-items: center;
    gap: 14px;
    text-align: right;
    line-height: 1.3;
    margin-bottom: 18px;
    white-space: nowrap;
  }
  .contact-list li:last-child { margin-bottom: 0; }
  .contact-list svg { width: 20px; height: 20px; flex: none; fill: var(--ink); }
  .license {
    position: absolute;
    left: 0; right: 0; top: 276px;
    text-align: center;
    font-weight: 600;
    font-size: 24px;
    color: var(--ink);
    white-space: nowrap;
  }
</style>
</head>
<body>

<section class="card card--front" aria-label="Card front">
  <svg class="card__stripes" viewBox="0 0 1034 590" preserveAspectRatio="none" aria-hidden="true">
    <g class="stripes-top">
      <polygon points="0,0 615,0 700,83 630,83 582,35 0,35" fill="var(--blue)"/>
      <polygon points="0,48 565,48 598,83 0,83" fill="var(--blue)"/>
      <polygon points="646,0 717,0 804,83 733,83" fill="var(--blue-2)"/>
      <polygon points="748,0 820,0 906,83 834,83" fill="var(--blue-3)"/>
      <polygon points="850,0 921,0 1008,83 936,83" fill="var(--blue-4)"/>
    </g>
    <rect x="0" y="555" width="1034" height="35" fill="var(--blue)"/>
  </svg>
  <div class="brand-mark">
    <span class="brand-mark__dot"></span>
    <span>Marlowe Holdings LLC</span>
  </div>
  <h1 class="company-name">Marlowe Holdings LLC</h1>
</section>

<section class="card card--back" aria-label="Card back">
  <svg class="card__stripes" viewBox="0 0 1034 590" preserveAspectRatio="none" aria-hidden="true">
    <g transform="translate(0,590) scale(1,-1)">
      <polygon points="0,0 615,0 700,69 630,69 582,29 0,29" fill="var(--blue)"/>
      <polygon points="0,35 565,35 598,69 0,69" fill="var(--blue)"/>
      <polygon points="646,0 717,0 804,69 733,69" fill="var(--blue-2)"/>
      <polygon points="748,0 820,0 906,69 834,69" fill="var(--blue-3)"/>
      <polygon points="850,0 921,0 1008,69 936,69" fill="var(--blue-4)"/>
    </g>
  </svg>
  <span class="side-tab"></span>

  <div class="brand-mark">
    <span class="brand-mark__dot"></span>
    <span>Marlowe Holdings LLC</span>
  </div>

  <h2 class="contact-name">Dean R Vossler</h2>
  <p class="contact-title">CHIEF EXECUTIVE MANAGER</p>

  <ul class="contact-list">
    <li>(555) 555-0148
      <svg viewBox="0 0 24 24" aria-hidden="true"><path d="M3 9c0-3 4-5 9-5s9 2 9 5v1.5h-4.5V8.5c-1.5-.6-3-.8-4.5-.8s-3 .2-4.5.8v2H3z"/><path d="M7 11l2-2h6l2 2 2 8H5z M12 12.5a2.5 2.5 0 1 0 0 5a2.5 2.5 0 1 0 0-5z"/></svg>
    </li>
    <li>dean.vossler@marloweholdingsffl.com
      <svg viewBox="0 0 24 24" aria-hidden="true"><path d="M2 5h20v14H2z M3.5 6.5l8.5 7 8.5-7" stroke="#fff" stroke-width="1.4" fill="var(--ink)"/></svg>
    </li>
    <li><span>412 N Ridgeview Lane #118<br>Elm Harbor, Il 60412</span>
      <svg viewBox="0 0 24 24" aria-hidden="true"><path d="M12 1.5a7 7 0 0 0-7 7c0 5 7 12 7 12s7-7 7-12a7 7 0 0 0-7-7zm0 4a3 3 0 1 1 0 6a3 3 0 1 1 0-6z"/><ellipse cx="12" cy="21.5" rx="5" ry="1.3" fill="none" stroke="var(--ink)" stroke-width="1.2"/></svg>
    </li>
  </ul>

  <p class="license">KPV FFL license number: 5-21-xxx-xx-xx-04519</p>
</section>

</body>
</html>
```